Business card design for crowd sourced review site.

I need a business card magnet design for an online, crowd-sourced, restaurant review site strictly for Kosher restaurants.
It is similar to WanderNotes but catering to a very particular crowd.
The markets it will be distributed in are flooded with business card fridge magnets so this needs to be eye-catching and unique. The Business name is PlateRanker
The website isnt finished but you can see the basic setup here
http://dining.brevtalo.com/

The second image i included is another logo design I liked and was thinking about using and decided I will probably also make a SECOND custom cut business card in the shape of that icon. Bonus if you can throw that in also.

Target Market(s)

Jewish consumers aged 20-35

Industry/Entity Type

Business

Contact Information for Business Card

see description.
Design should not be too crowded and should in eye-catching. Will mainly be used as fridge magnets.

Requirements
Must have
• Website address. logo.
Nice to have
• tagline. (The Definitive guide to kosher dining for the Kosher consumer)
• Im not a professional but I personally think the color blue goes along with this concept. ill leave it to you to decide.
Should not have
• any religious symbols.

```html
<!DOCTYPE html>
<html lang="en">
<head>
<meta charset="utf-8">
<title>PlateRanker Business Card</title>
<link href="https://fonts.googleapis.com/css2?family=Open+Sans:wght@400;600&display=swap" rel="stylesheet">
<style>
  :root {
    --backdrop: #ece9e6;
    --card-white: #ffffff;
    --brand-orange: #e8461e;
    --brand-orange-light: #ef5a2e;
    --text-light: #ffffff;
    --shadow: rgba(0, 0, 0, 0.18);
  }
  * { margin: 0; padding: 0; box-sizing: border-box; }
  html, body {
    width: 1200px;
    height: 1200px;
    overflow: hidden;
    background: var(--backdrop);
    font-family: "Open Sans", Arial, sans-serif;
  }
  .stage {
    width: 1200px;
    height: 1200px;
    display: flex;
    align-items: center;
    justify-content: center;
  }
  .business-card {
    width: 1000px;
    height: 572px;
    background: var(--card-white);
    box-shadow: 0 18px 40px var(--shadow);
    display: flex;
    flex-direction: column;
    overflow: hidden;
  }
  .brand-area {
    height: 300px;
    display: flex;
    align-items: center;
    justify-content: center;
    gap: 22px;
  }
  .brand-dot {
    width: 70px;
    height: 70px;
    border-radius: 50%;
    background: var(--brand-orange);
  }
  .brand-name {
    font-size: 78px;
    font-weight: 600;
    color: var(--brand-orange);
    letter-spacing: -1px;
  }
  .contact-band {
    flex: 1;
    background: linear-gradient(180deg, var(--brand-orange) 0%, var(--brand-orange-light) 100%);
    display: flex;
    align-items: center;
    padding-left: 250px;
    color: var(--text-light);
  }
  .person-name {
    font-size: 46px;
    font-weight: 400;
    width: 210px;
  }
  .divider {
    width: 3px;
    height: 170px;
    background: var(--text-light);
    margin: 0 34px 0 10px;
  }
  .contact-list {
    list-style: none;
    display: flex;
    flex-direction: column;
    gap: 8px;
    font-size: 30px;
    line-height: 1.2;
  }
  .contact-item {
    display: flex;
    align-items: center;
    gap: 16px;
  }
  .contact-icon {
    width: 26px;
    height: 26px;
    flex: none;
  }
</style>
</head>
<body>
  <main class="stage">
    <section class="business-card">
      <header class="brand-area">
        <span class="brand-dot"></span>
        <span class="brand-name">PlateRanker</span>
      </header>
      <div class="contact-band">
        <p class="person-name">Miriam</p>
        <span class="divider"></span>
        <ul class="contact-list">
          <li class="contact-item">
            <svg class="contact-icon" viewBox="0 0 26 26" aria-hidden="true">
              <rect x="0" y="0" width="26" height="26" rx="3" fill="#fff"/>
              <rect x="8" y="4" width="10" height="18" rx="2" fill="none" stroke="#e8461e" stroke-width="2"/>
              <circle cx="13" cy="19" r="1.3" fill="#e8461e"/>
            </svg>
            <span>5550142876</span>
          </li>
          <li class="contact-item">
            <svg class="contact-icon" viewBox="0 0 26 26" aria-hidden="true">
              <rect x="0" y="0" width="26" height="26" rx="3" fill="#fff"/>
              <path d="M5 11 Q13 4 21 11 L19 13 L16 11 L10 11 L7 13 Z" fill="#e8461e"/>
              <rect x="7" y="13" width="12" height="8" rx="1.5" fill="#e8461e"/>
            </svg>
            <span>0491 555 027</span>
          </li>
          <li class="contact-item">
            <svg class="contact-icon" viewBox="0 0 26 26" aria-hidden="true">
              <rect x="0" y="0" width="26" height="26" rx="3" fill="#fff"/>
              <circle cx="13" cy="13" r="8" fill="none" stroke="#e8461e" stroke-width="2"/>
              <ellipse cx="13" cy="13" rx="3.5" ry="8" fill="none" stroke="#e8461e" stroke-width="1.5"/>
              <line x1="5" y1="13" x2="21" y2="13" stroke="#e8461e" stroke-width="1.5"/>
            </svg>
            <span>www.dining.brevtalo.com</span>
          </li>
        </ul>
      </div>
    </section>
  </main>
</body>
</html>
```